Business Card Design

I need a business card designed for my business.

The company name is Miles Renford Collective

It has four brands underneath it. They are:
- MR Occasions
- MR Athletic Journeys
- MRC Stewardship
- Dove Draftworks

I have attached all logo items, as well as our last business card.

I look forward to seeing your designs.

Industry/Entity Type

Business

Colors
eb1f27
0355a3

Requirements
Must have
• Our contact details as per the front page of our previous business card.

```html
<!DOCTYPE html>
<html lang="en">
<head>
<meta charset="utf-8">
<title>Miles Renford Collective – Business Card</title>
<link rel="stylesheet" href="https://fonts.googleapis.com/css2?family=Marcellus+SC&display=swap">
<style>
  :root {
    --card-white: #ffffff;
    --band-red: #9e1c22;
    --brand-blue: #0355a3;
    --brand-red: #eb1f27;
    --text-light: #fbf3f0;
    --text-shadow: rgba(40, 0, 0, 0.75);
  }
  html, body {
    margin: 0;
    padding: 0;
    overflow: hidden;
    background: var(--card-white);
  }
  .card {
    position: relative;
    width: 1200px;
    height: 704px;
    overflow: hidden;
    background: var(--card-white);
    font-family: "Marcellus SC", serif;
  }
  .brand {
    position: absolute;
    left: 230px;
    top: 100px;
    display: flex;
    align-items: center;
    gap: 42px;
  }
  .brand-dot {
    width: 140px;
    height: 170px;
    display: block;
  }
  .brand-name {
    margin: 0;
    color: var(--brand-blue);
    font-weight: 400;
    line-height: 1.05;
    font-size: 58px;
    letter-spacing: 1px;
  }
  .brand-name .brand-line {
    display: block;
  }
  .contact-band {
    position: absolute;
    left: 0;
    top: 366px;
    width: 1200px;
    height: 338px;
    background: var(--band-red);
    color: var(--text-light);
    text-align: center;
    text-shadow: 2px 3px 4px var(--text-shadow);
  }
  .contact-band p {
    position: absolute;
    left: 0;
    width: 100%;
    margin: 0;
    line-height: 1;
    transform: translate(-30px, -50%);
  }
  .principal { top: 38px; font-size: 40px; letter-spacing: 1px; }
  .address   { top: 93px; font-size: 38px; word-spacing: 14px; letter-spacing: 1px; }
  .contact-label { top: 147px; font-size: 28px; letter-spacing: 1px; }
  .phone-office  { top: 183px; font-size: 31px; letter-spacing: 1px; }
  .phone-mobile  { top: 224px; font-size: 31px; letter-spacing: 1px; }
  .email         { top: 265px; font-size: 28px; letter-spacing: 0.5px; }
</style>
</head>
<body>
  <main class="card">
    <header class="brand">
      <svg class="brand-dot" viewBox="0 0 140 170" aria-hidden="true">
        <ellipse cx="70" cy="85" rx="66" ry="80" fill="var(--brand-blue)"/>
      </svg>
      <h1 class="brand-name">
        <span class="brand-line">Miles Renford</span>
        <span class="brand-line">Collective</span>
      </h1>
    </header>

    <section class="contact-band">
      <p class="principal">Principle: Miles Renford</p>
      <p class="address">P.O. Box 418 Halden ACT 2619</p>
      <p class="contact-label">Contact :</p>
      <p class="phone-office">+61 2 6200 4815</p>
      <p class="phone-mobile">+61 455 302 871</p>
      <p class="email">Miles@MilesRenfordCollective.com.au</p>
    </section>
  </main>
</body>
</html>
```